Design a blog page showing lists of latest posts.

I want to design my blog home page. This page will show a list of my latest blog posts.

The site URL is velrunok.com and I have already given a basic structure to it. Please visit and have a look at it.

The color scheme of the design should be black (or grey) and white.

Below the top header I want an opt-in form and below that list of my blog posts. Then pagination and then a bottom section, that will show my two products. Please design these two boxes without any image.

Please avoid using any background image. If necessary, use any image without a character or person. Avoid using the sidebar.

Make it beautiful with the use of typography and white spaces.

I am open to any new creative ideas. Let me know if you have any?

1 page

• Sidebar

```html
<!DOCTYPE html>
<html lang="en">
<head>
<meta charset="utf-8">
<title>Top Recommended Resources</title>
<link href="https://fonts.googleapis.com/css2?family=Montserrat:wght@400;500;600;700&display=swap" rel="stylesheet">
<style>
  :root {
    --ink: #000000;
    --heading: #2f2f2f;
    --body: #3a3a3a;
    --muted: #6b6b6b;
    --byline: #9a9a9a;
    --panel: #f2f2f2;
    --footer-bg: #333333;
    --footer-text: #ffffff;
    --page: #ffffff;
  }
  * { margin: 0; padding: 0; box-sizing: border-box; }
  html, body { width: 1200px; height: 813px; overflow: hidden; background: var(--page); }
  body { font-family: 'Montserrat', sans-serif; position: relative; }

  .section-title {
    position: absolute; left: 0; top: 29px; width: 1200px;
    text-align: center; font-size: 29px; font-weight: 700;
    line-height: 34px; letter-spacing: 1.2px; color: var(--heading);
  }
  .section-rule {
    position: absolute; left: 557px; top: 109px; width: 82px; height: 1px;
    background: var(--heading);
  }
  .section-intro {
    position: absolute; left: 300px; top: 139px; width: 600px;
    text-align: center; font-size: 11px; line-height: 21px;
    color: var(--body); letter-spacing: 0.4px;
  }

  .product-panel { position: absolute; top: 256px; height: 334px; background: var(--panel); }
  .product-panel--left { left: 362px; width: 185px; }
  .product-panel--right { left: 654px; width: 168px; }

  .product { position: absolute; top: 336px; }
  .product--left { left: 173px; text-align: left; }
  .product--right { right: 172px; text-align: right; }

  .product-byline {
    font-size: 15px; font-weight: 600; letter-spacing: 6.1px;
    color: var(--byline); line-height: 24px; padding-left: 4px; white-space: nowrap;
  }
  .product--right .product-byline { padding-left: 0; margin-right: -6px; }
  .product-title {
    margin-top: 9px; font-size: 26px; font-weight: 700;
    line-height: 36px; color: var(--ink); letter-spacing: 0.4px; white-space: nowrap;
  }
  .product-rule { position: absolute; top: 120px; width: 82px; height: 1px; background: var(--ink); }
  .product--left .product-rule { left: 1px; }
  .product--right .product-rule { right: 1px; }

  .product-text {
    position: absolute; top: 115px;
    font-size: 10.4px; line-height: 18.8px; color: var(--muted); letter-spacing: 0.15px;
    white-space: nowrap;
  }
  .product--left .product-text { left: 107px; }
  .product--right .product-text { right: 104px; }

  .product-link {
    position: absolute; top: 197px; display: flex; align-items: center; gap: 6px;
    font-size: 8.5px; font-weight: 700; letter-spacing: 1.2px; color: var(--ink);
    text-decoration: none; white-space: nowrap;
  }
  .product--left .product-link { left: 107px; }
  .product--right .product-link { right: 104px; }

  .site-footer {
    position: absolute; left: 0; top: 682px; width: 1200px; height: 131px;
    background: var(--footer-bg); color: var(--footer-text);
  }
  .footer-nav { position: absolute; top: 37px; left: 0; width: 1200px; height: 14px; }
  .footer-nav a {
    position: absolute; font-size: 10.5px; font-weight: 700; letter-spacing: 0.8px;
    color: var(--footer-text); text-decoration: none;
  }
  .copyright {
    position: absolute; top: 63px; width: 1200px; text-align: center;
    font-size: 9.5px; letter-spacing: 1px;
  }
</style>
</head>
<body>
  <h2 class="section-title">TOP RECOMMENDED<br>RESOURCES</h2>
  <div class="section-rule"></div>
  <p class="section-intro">Lorem ipsum dolor sit amet, consectetur adipiscing elit, sed do eiusmod tempor incididunt ut<br>labore et dolore magna aliqua. Ut enim ad minim</p>

  <div class="product-panel product-panel--left"></div>
  <div class="product-panel product-panel--right"></div>

  <article class="product product--left">
    <p class="product-byline">BY TOMAS REYVEL</p>
    <h3 class="product-title">THE PQM TRAINING<br>PROGRAM</h3>
    <div class="product-rule"></div>
    <p class="product-text">Lorem ipsum dolor sit amet, consectetur<br>adipisicing elit, sed do eiusmod tempor<br>incididunt ut labore et dolore magna aliqua.</p>
    <a class="product-link" href="#">VIEW MORE
      <svg width="16" height="9" viewBox="0 0 16 9"><path d="M0 4.5H14M10.5 1L14.5 4.5L10.5 8" fill="none" stroke="#000" stroke-width="1.4"/></svg>
    </a>
  </article>

  <article class="product product--right">
    <p class="product-byline">BY TOMAS REYVEL</p>
    <h3 class="product-title">THE PQM EXAM<br>PREPARATION TOOL</h3>
    <div class="product-rule"></div>
    <p class="product-text">Lorem ipsum dolor sit amet, consectetur<br>adipisicing elit, sed do eiusmod tempor<br>incididunt ut labore et dolore magna aliqua.</p>
    <a class="product-link" href="#">VIEW MORE
      <svg width="16" height="9" viewBox="0 0 16 9"><path d="M0 4.5H14M10.5 1L14.5 4.5L10.5 8" fill="none" stroke="#000" stroke-width="1.4"/></svg>
    </a>
  </article>

  <footer class="site-footer">
    <nav class="footer-nav">
      <a href="#" style="left:391px">FAQS</a>
      <a href="#" style="left:458px">PDU</a>
      <a href="#" style="left:511px">BOOKS</a>
      <a href="#" style="left:582px">ABOUT</a>
      <a href="#" style="left:649px">AFFILIATES</a>
      <a href="#" style="left:747px">CONTACT</a>
    </nav>
    <p class="copyright">Copyright 2020 , All rights reserved</p>
  </footer>
</body>
</html>
```